Copperfox Billboard

Please design a billboard using my photos and logos.
For photo of truck please crop the truck itself out and not have the trees / dirt in photo.
Please put " Best Prices in Sevier County"
Please put " 30-yard Dumpsters Starting at 600.00"
Please put " 16-yard Dumpsters Starting at 300.0"
Please put " Delivery and Pickup 7 Days a week"
Billboard size will be 10 ft tall 30 ft wide

```html
<!DOCTYPE html>
<html lang="en">
<head>
<meta charset="utf-8">
<title>Copperfox Dumpsters Billboard</title>
<link href="https://fonts.googleapis.com/css2?family=Montserrat:wght@600;700;800;900&display=swap" rel="stylesheet">
<style>
  :root {
    --purple: #7b3fa6;
    --purple-mid: #6a2f94;
    --purple-deep: #34174d;
    --ink: #111111;
    --paper: #ffffff;
    --stage: #e9e6ee;
  }
  html, body {
    margin: 0;
    padding: 0;
    width: 1200px;
    height: 824px;
    overflow: hidden;
    background: var(--stage);
    font-family: "Montserrat", Arial, sans-serif;
  }
  .billboard {
    position: absolute;
    left: 30px;
    top: 222px;
    width: 1140px;
    height: 380px;
    background: var(--paper);
    overflow: hidden;
    box-shadow: 0 10px 30px rgba(40, 20, 60, 0.25);
  }
  .billboard__shapes {
    position: absolute;
    inset: 0;
  }
  .brand {
    position: absolute;
    left: 150px;
    top: 26px;
    color: var(--purple-deep);
    font-weight: 900;
    line-height: 1;
    text-transform: uppercase;
  }
  .brand__name {
    font-size: 66px;
    letter-spacing: 1px;
  }
  .brand__sub {
    font-size: 30px;
    letter-spacing: 2px;
    text-align: right;
    margin-top: 4px;
  }
  .ribbon {
    position: absolute;
    left: 104px;
    top: 150px;
    color: var(--paper);
    font-weight: 800;
    font-size: 26px;
    line-height: 40px;
    width: 460px;
    text-align: center;
  }
  .prices {
    position: absolute;
    left: 24px;
    top: 196px;
    color: var(--ink);
    font-weight: 800;
    font-size: 29px;
    line-height: 36px;
  }
  .prices__line--second { padding-left: 16px; }
  .service-band {
    position: absolute;
    left: 24px;
    top: 276px;
    color: var(--paper);
    font-weight: 900;
    font-size: 22px;
    letter-spacing: 1px;
    line-height: 30px;
    text-transform: uppercase;
  }
  .service-band__accent { color: var(--purple); }
  .contact-phone {
    position: absolute;
    left: 24px;
    top: 318px;
    display: flex;
    align-items: center;
    gap: 10px;
    color: var(--paper);
    font-weight: 800;
    font-size: 42px;
    line-height: 50px;
  }
  .contact-web {
    position: absolute;
    left: 462px;
    top: 328px;
    display: flex;
    align-items: center;
    gap: 10px;
    color: var(--paper);
    font-weight: 700;
    font-size: 24px;
    line-height: 34px;
  }
  .contact-web__tld { color: #b77ee0; }
  .truck-photo {
    position: absolute;
    left: 640px;
    top: 100px;
    width: 440px;
    height: 240px;
    border-radius: 6px;
    background: linear-gradient(100deg, #f4f4f6 0%, #dcdce2 45%, #4a2a6a 70%, #3a1d57 100%);
  }
</style>
</head>
<body>
  <div class="billboard">
    <svg class="billboard__shapes" width="1140" height="380" viewBox="0 0 1140 380" aria-hidden="true">
      <polygon points="770,0 1140,0 1140,380 920,380" fill="var(--purple)"/>
      <polygon points="770,0 800,0 940,380 905,380" fill="var(--ink)"/>
      <polygon points="860,260 905,380 860,380 820,270" fill="var(--paper)"/>
      <polygon points="0,270 820,270 834,306 0,306" fill="var(--ink)"/>
      <polygon points="0,306 834,306 860,380 0,380" fill="var(--purple-deep)"/>
      <polygon points="0,306 410,306 440,380 0,380" fill="var(--purple)"/>
      <polygon points="96,150 580,150 560,170 580,190 96,190 116,170" fill="var(--purple)"/>
    </svg>

    <div class="brand">
      <div class="brand__name">Copperfox</div>
      <div class="brand__sub">Dumpsters</div>
    </div>

    <div class="ribbon">Best Prices in Sevier County</div>

    <div class="prices">
      <div class="prices__line">30-yard Dumpsters Starting at 600.00</div>
      <div class="prices__line prices__line--second">16-yard Dumpsters Starting at 300.0</div>
    </div>

    <div class="service-band">Delivery <span class="service-band__accent">and</span> Pickup 7 Days a Week</div>

    <div class="contact-phone">
      <svg width="30" height="30" viewBox="0 0 24 24" aria-hidden="true">
        <path d="M6.6 10.8a15.1 15.1 0 0 0 6.6 6.6l2.2-2.2a1 1 0 0 1 1-.25 11.4 11.4 0 0 0 3.6.57 1 1 0 0 1 1 1V20a1 1 0 0 1-1 1A17 17 0 0 1 3 4a1 1 0 0 1 1-1h3.5a1 1 0 0 1 1 1c0 1.25.2 2.45.57 3.57a1 1 0 0 1-.25 1z" fill="var(--paper)"/>
      </svg>
      <span>865 555 0142</span>
    </div>

    <div class="contact-web">
      <svg width="28" height="28" viewBox="0 0 24 24" aria-hidden="true" fill="none" stroke="#b77ee0" stroke-width="1.6">
        <circle cx="12" cy="12" r="10"/>
        <ellipse cx="12" cy="12" rx="4.5" ry="10"/>
        <line x1="2" y1="12" x2="22" y2="12"/>
        <line x1="4" y1="7" x2="20" y2="7"/>
        <line x1="4" y1="17" x2="20" y2="17"/>
      </svg>
      <span>copperfoxdumpsters<span class="contact-web__tld">.com</span></span>
    </div>

    <div class="truck-photo" role="img" aria-label="Photo of a white roll-off truck carrying a purple dumpster container, cut out from its background"></div>
  </div>
</body>
</html>
```